flatrotate.co.uk landing page website design

Hi designers, I would like a custom designed landing page very similar to www.dwellingtrader.co.uk. It represents a happy place, sunny days and people swapping homes. I would like this done just like theres but our own design but a similar layout as theres.

I would like the 3 reasons to use us to be

Connect to thousands of other people in your area looking for a home swap

Our service is Completely free unlike most other exchange websites.

Find a exchange within 30 days!*

Thank you all,

Hi Everyone, I need the designs to represent london if possible like one of the designers has done for anyone else being in with a chance to win. Please check out the design by KR with the london look. I still like some of the others and they may win but i need to give this a try please.

Target Market(s)

Council house tenants

Coding

Coded - Design and coding required

Number of Pages Required

1 page

Requirements
Must have
• Custom designed landing page showing all the elements that www.dwellingtrader.co.uk use, The blue sky, and the land it shows with houses and people representing people swapping house. It can not be the same as them but can be similar concept with our own custom design and colour scheme ect.

please create 3 bubbles for speech from people. Please add the following quotes. "Its time we upsize"
"lets try and downsize and save money" "shall we move house?"
Would like 2 blocks of flats in a similar way dwelling trader.co.uk show the houses.
Nice to have

Should not have
• Same colour scheme as dwelling trader apart from the blue sky

```html
<!DOCTYPE html>
<html lang="en">
<head>
<meta charset="utf-8">
<title>Flat Rotate – Swap Your Social Home</title>
<link rel="stylesheet" href="https://fonts.googleapis.com/css2?family=Raleway:wght@600;700&family=Open+Sans:wght@400;600;700&display=swap">
<style>
:root{
  --sky-top:#76daf6;
  --sky-low:#d6eef6;
  --meadow:#3cb830;
  --meadow-deep:#239a1e;
  --navy:#0b55a3;
  --red:#d9363e;
  --teal:#13e2b8;
  --ink:#1d1d1d;
  --grey:#666;
  --green-1:#a2d31a;
  --green-2:#7fbd26;
  --green-bar:#6ea31d;
  --white:#fff;
}
*{box-sizing:border-box;margin:0;padding:0}
html,body{width:1200px;height:2273px;overflow:hidden}
body{position:relative;background:var(--white);font-family:'Open Sans',Arial,sans-serif;color:var(--ink)}
.hero{position:absolute;left:0;top:0;width:1200px;height:1134px;
  background:linear-gradient(180deg,var(--sky-top) 0,#9fe2f5 260px,var(--sky-low) 520px,#eef7e8 620px)}
.hero-scene{position:absolute;left:0;top:520px;width:1200px;height:614px;
  background:linear-gradient(180deg,rgba(214,238,246,0) 0,#a6dc8c 140px,var(--meadow) 300px,var(--meadow-deep) 614px);
  clip-path:polygon(0 0,100% 0,100% 525px,80% 545px,55% 575px,30% 600px,10% 612px,0 614px)}
.brand{position:absolute;left:100px;top:56px;display:flex;align-items:center;gap:10px;
  font-family:'Raleway',sans-serif;font-weight:700;font-size:28px;color:var(--ink)}
.brand-mark{width:34px;height:34px;background:var(--red);border-radius:4px}
.btn{position:absolute;display:flex;align-items:center;justify-content:center;border-radius:40px;
  font-family:'Raleway',sans-serif;font-weight:700;text-transform:uppercase}
.btn-login{left:775px;top:54px;width:148px;height:54px;background:var(--navy);color:var(--white);font-size:19px;gap:6px}
.btn-register{left:938px;top:54px;width:147px;height:54px;border:2px solid var(--navy);color:var(--navy);font-size:19px;gap:6px}
.hero-title{position:absolute;top:160px;left:0;width:1200px;text-align:center;
  font-family:'Raleway',sans-serif;font-weight:700;font-size:60px;color:#161616}
.search{position:absolute;left:114px;top:265px;width:972px;height:127px;background:var(--white);border-radius:3px;
  box-shadow:0 4px 14px rgba(0,0,0,.12)}
.field{position:absolute;top:18px;width:260px}
.field label{display:block;font-size:16px;color:#333;letter-spacing:.3px;margin-bottom:10px}
.field .input{height:52px;border:1px solid #9a9a9a;display:flex;align-items:center;padding:0 16px;font-size:15px;color:#777;gap:8px;position:relative}
.field .caret{position:absolute;right:20px;top:22px;border-left:6px solid transparent;border-right:6px solid transparent;border-top:7px solid #333}
.btn-search{left:821px;top:46px;width:135px;height:57px;background:var(--red);color:var(--white);font-size:21px;border-radius:30px}
.join{position:absolute;top:424px;left:0;width:1200px;text-align:center;font-size:30px;color:#222}
.join strong{color:var(--red);font-weight:700}
.btn-tenant{left:301px;top:506px;width:289px;height:62px;background:var(--navy);color:var(--white);font-size:20px}
.btn-landlord{left:610px;top:506px;width:288px;height:62px;border:2px solid var(--navy);color:var(--navy);font-size:20px;background:rgba(255,255,255,.15)}
.bubble{position:absolute;background:var(--teal);color:var(--white);font-weight:600;text-align:center;
  display:flex;align-items:center;justify-content:center;line-height:1.2;border-radius:50%;padding:0 18px}
.bubble-upsize{left:198px;top:893px;width:238px;height:124px;font-size:28px}
.bubble-downsize{left:440px;top:700px;width:260px;height:130px;font-size:24px}
.bubble-move{left:795px;top:804px;width:216px;height:146px;font-size:27px}
.why-title{position:absolute;top:1198px;left:0;width:1200px;text-align:center;
  font-family:'Raleway',sans-serif;font-weight:700;font-size:53px;color:#222}
.why-intro{position:absolute;top:1286px;left:170px;width:860px;text-align:center;font-size:16px;line-height:31px;color:var(--grey)}
.reason{position:absolute;top:1436px;width:304px;height:304px;border-radius:50%;background:var(--white);
  box-shadow:0 6px 22px rgba(0,0,0,.1)}
.reason-ring{position:absolute;left:17px;top:17px;width:270px;height:270px;border-radius:50%;border:4px solid var(--navy);
  display:flex;flex-direction:column;align-items:center;padding-top:40px}
.reason-ring.red{border-color:var(--red)}
.reason-icon{height:66px;display:flex;align-items:center;justify-content:center}
.reason p{margin-top:22px;font-size:19px;line-height:29px;text-align:center;color:#222;padding:0 24px}
.footer{position:absolute;left:0;top:1782px;width:1200px;height:491px;
  background:linear-gradient(180deg,var(--white) 0,#e2f1b9 60px,var(--green-1) 140px,var(--green-2) 405px)}
.footer-scene{position:absolute;left:0;top:0;width:1200px;height:145px;
  background:linear-gradient(180deg,rgba(160,211,26,0) 0,rgba(160,211,26,.55) 100%)}
.col{position:absolute;top:180px;color:var(--white)}
.col h3{font-family:'Raleway',sans-serif;font-weight:700;font-size:19px;text-transform:uppercase;margin-bottom:20px}
.col p,.col li{font-size:14px;line-height:23px;list-style:none}
.col li{margin-bottom:4px}
.col-about{left:111px;width:310px}
.col-links{left:445px}
.col-signup{left:619px;width:270px}
.col-contact{left:916px}
.email-input{margin-top:21px;width:265px;height:36px;background:var(--white);display:flex;align-items:center;gap:8px;padding:0 14px;font-size:14px;color:#888}
.btn-signup{position:static;margin-top:14px;width:120px;height:43px;background:var(--red);color:var(--white);font-size:17px}
.contact-row{display:flex;gap:12px;align-items:flex-start;font-size:14px;line-height:23px;margin-bottom:22px}
.contact-row svg{flex:none;margin-top:4px}
.bottom-bar{position:absolute;left:0;top:405px;width:1200px;height:86px;background:var(--green-bar);color:var(--white)}
.copyright{position:absolute;left:113px;top:36px;font-size:15px}
.social{position:absolute;top:22px;width:42px;height:42px;border:2px solid var(--white);border-radius:50%}
</style>
</head>
<body>

<header class="hero">
  <div class="hero-scene" role="img" aria-label="Sunny landscape with green hills, white houses and blocks of flats, trees, a lake, a rising sun and silhouettes of families, walkers and a cyclist"></div>

  <div class="brand"><span class="brand-mark"></span>Flat Rotate</div>
  <div class="btn btn-login">
    <svg width="14" height="16" viewBox="0 0 14 16"><rect x="1" y="7" width="12" height="9" rx="1" fill="#fff"/><path d="M4 7V5a3 3 0 0 1 6 0v2" stroke="#fff" stroke-width="2" fill="none"/></svg>Login</div>
  <div class="btn btn-register">
    <svg width="16" height="16" viewBox="0 0 16 16"><path d="M2 14l1-4 8-8 3 3-8 8z" fill="#0b55a3"/></svg>Register</div>

  <h1 class="hero-title">Swap Your Social Home</h1>

  <form class="search">
    <div class="field" style="left:20px">
      <label>LOCATION</label>
      <div class="input"><svg width="10" height="14" viewBox="0 0 10 14"><path d="M5 0a5 5 0 0 1 5 5c0 4-5 9-5 9S0 9 0 5a5 5 0 0 1 5-5z" fill="#777"/><circle cx="5" cy="5" r="2" fill="#fff"/></svg>Postcode</div>
    </div>
    <div class="field" style="left:287px">
      <label>BEDROOMS</label>
      <div class="input">Any<span class="caret"></span></div>
    </div>
    <div class="field" style="left:553px">
      <label>MAX. RENT (£ PER MONTH)</label>
      <div class="input">Any<span class="caret"></span></div>
    </div>
    <div class="btn btn-search">Search</div>
  </form>

  <p class="join">Join <strong>700,000</strong> other social tenants on Flat Rotate</p>

  <div class="btn btn-tenant">Are you a tenant?</div>
  <div class="btn btn-landlord">Are you a landlord?</div>

  <div class="bubble bubble-upsize">Its time<br>we upsize</div>
  <div class="bubble bubble-downsize">Lets try and downsize<br>and save money</div>
  <div class="bubble bubble-move">Shall we<br>move house?</div>
</header>

<section class="why">
  <h2 class="why-title">Why Choose Flat Rotate?</h2>
  <p class="why-intro">Nemo enim ipsam voluptatem quia voluptas sit aspernatur aut odit aut fugit, sed quia consequuntur magni dolores eos qui ratione voluptatem sequi nesciunt. Neque porro quisquam est, qui dolorem ipsum quia dolor sit amet, consectetur, adipisci velit, sed quia non numquam eius modi.</p>

  <div class="reason" style="left:113px">
    <div class="reason-ring">
      <div class="reason-icon"><svg width="58" height="58" viewBox="0 0 60 60"><circle cx="30" cy="30" r="29" fill="#0b55a3"/><ellipse cx="30" cy="30" rx="12" ry="28" fill="none" stroke="#fff" stroke-width="2"/><path d="M2 30h56M6 16h48M6 44h48" stroke="#fff" stroke-width="2"/></svg></div>
      <p>Connect to thousands of other people in your area looking for a home swap</p>
    </div>
  </div>

  <div class="reason" style="left:449px">
    <div class="reason-ring red">
      <div class="reason-icon"><svg width="76" height="66" viewBox="0 0 78 68"><circle cx="28" cy="36" r="15" fill="none" stroke="#d9363e" stroke-width="10" stroke-dasharray="5 4"/><circle cx="28" cy="36" r="12" fill="#d9363e"/><circle cx="28" cy="36" r="5" fill="#fff"/><circle cx="60" cy="14" r="8" fill="#d9363e"/><circle cx="60" cy="14" r="3" fill="#fff"/><circle cx="62" cy="54" r="8" fill="#d9363e"/><circle cx="62" cy="54" r="3" fill="#fff"/></svg></div>
      <p>Our service is Completely free unlike most other exchange websites</p>
    </div>
  </div>

  <div class="reason" style="left:781px">
    <div class="reason-ring">
      <div class="reason-icon"><svg width="70" height="54" viewBox="0 0 72 56"><path d="M2 14h54" stroke="#0b55a3" stroke-width="8"/><path d="M52 2l18 12-18 12z" fill="#0b55a3"/><path d="M70 42H16" stroke="#0b55a3" stroke-width="8"/><path d="M20 30L2 42l18 12z" fill="#0b55a3"/></svg></div>
      <p>Find a exchange within<br>30 days!*</p>
    </div>
  </div>
</section>

<footer class="footer">
  <div class="footer-scene" role="img" aria-label="Green silhouettes of a family, a cyclist, grass, a tree, butterflies and houses"></div>

  <div class="col col-about">
    <h3>About</h3>
    <p>Nemo enim ipsam voluptatem quia voluptas sit aspernatur aut odit aut fugit, sed quia consequuntur magni dolores eos.</p>
  </div>

  <div class="col col-links">
    <h3>Quick Links</h3>
    <ul><li>Terms &amp; Conditions</li><li>Sitemap</li><li>Disclaimer</li><li>Privacy Policy</li></ul>
  </div>

  <div class="col col-signup">
    <h3>Email Sign Up</h3>
    <p>Enter your email address to get information about us</p>
    <div class="email-input"><svg width="14" height="10" viewBox="0 0 14 10"><rect width="14" height="10" fill="#888"/><path d="M0 0l7 5 7-5" stroke="#fff" fill="none"/></svg>Email address</div>
    <div class="btn btn-signup">Sign up</div>
  </div>

  <div class="col col-contact">
    <h3>Contact Us</h3>
    <div class="contact-row"><svg width="10" height="14" viewBox="0 0 10 14"><path d="M5 0a5 5 0 0 1 5 5c0 4-5 9-5 9S0 9 0 5a5 5 0 0 1 5-5z" fill="#fff"/><circle cx="5" cy="5" r="2" fill="#7fbd26"/></svg><span>Harbour Lane 14<br>2210 Westmere</span></div>
    <div class="contact-row"><svg width="14" height="14" viewBox="0 0 14 14"><path d="M3 0l3 3-2 2c1 2 3 4 5 5l2-2 3 3-2 3C6 14 0 8 0 2z" fill="#fff"/></svg><span>+1 555 010 200</span></div>
    <div class="contact-row"><svg width="16" height="12" viewBox="0 0 16 12"><rect width="16" height="12" fill="#fff"/><path d="M0 0l8 6 8-6" stroke="#7fbd26" fill="none"/></svg><span>info@flatrotate.com</span></div>
  </div>

  <div class="bottom-bar">
    <p class="copyright">© Copyright 2020: Flat Rotate. All rights reserved</p>
    <span class="social" style="left:896px"></span>
    <span class="social" style="left:944px"></span>
    <span class="social" style="left:995px"></span>
    <span class="social" style="left:1047px"></span>
  </div>
</footer>

</body>
</html>
```